Meridian Sound Wellness LLC Card Design

Need business card with a logo for a hearing aid sales and audiology business. We have two Hearing Instrument Specialists and one Audiologist on staff. Over 25 years in business. Locally owned and operated. Financing available. Most insurances accepted.

Meridian Sound Wellness LLC
48730 W Linden Row, Suite 9
Spokane, WA 99481
509-617-2085
www.meridiansoundnorth.example

Manager
Tobias Wrenfield HIS COHC
License #81729046

Target Market(s)

50yr old + people with a hearing loss.

Industry/Entity Type

Business

Contact Information for Business Card

48730 W Linden Row, Suite 9
Spokane, WA 99481
509-617-2085
www.meridiansoundnorth.example

Manager
Tobias Wrenfield HIS COHC
NRPL #81729046

Font styles to use
Serif
Sans Serif

Requirements
Must have
• Business name, Tobias's name and title(s) and contact information, License #, web address
Nice to have
Should not have

```html
<!DOCTYPE html>
<html lang="en">
<head>
<meta charset="utf-8">
<title>Meridian Sound Wellness LLC – Business Card</title>
<link rel="stylesheet" href="https://fonts.googleapis.com/css2?family=Cinzel:wght@400&family=Open+Sans:wght@400;600;700&display=swap">
<style>
  :root {
    --backdrop: #161616;
    --card-white: #f3f3f3;
    --brand-green: #4f9a1f;
    --name-green: #3a8a12;
    --ink: #1c1c1c;
    --green-top: #6cb42e;
    --green-bottom: #0d780b;
    --on-green: #ffffff;
  }
  * { margin: 0; padding: 0; box-sizing: border-box; }
  html, body {
    width: 1200px; height: 900px; overflow: hidden;
    background: var(--backdrop);
  }
  .stage { position: relative; width: 1200px; height: 900px; }
  .card {
    position: absolute; top: 184px;
    width: 302px; height: 490px;
    border-radius: 12px; overflow: hidden;
  }
  .card--front { left: 299px; background: var(--card-white); }
  .card--back {
    left: 645px; width: 305px;
    background: linear-gradient(180deg, var(--green-top) 0%, var(--green-top) 25%, var(--green-bottom) 100%);
  }
  .brand {
    position: absolute; left: 0; right: 0;
    text-align: center;
    font-family: "Cinzel", Georgia, serif;
    font-weight: 400;
    line-height: 1.15;
  }
  .card--front .brand { top: 122px; font-size: 19px; color: var(--brand-green); }
  .brand-dot {
    position: absolute; left: 50%; top: 48px;
    width: 56px; height: 56px; margin-left: -28px;
    border-radius: 50%; background: var(--brand-green);
  }
  .contact {
    position: absolute; left: 0; right: 0; top: 298px;
    text-align: center;
    font-family: "Open Sans", Arial, sans-serif;
    color: var(--ink);
    font-size: 13px; line-height: 17px;
  }
  .contact__name { font-size: 16px; font-weight: 700; color: var(--name-green); line-height: 20px; }
  .contact__creds { font-size: 13px; font-weight: 600; }
  .contact__block { margin-top: 12px; }
  .contact__license { margin-top: 14px; font-weight: 700; }
  .card--back .brand { top: 406px; font-size: 19px; color: var(--on-green); }
</style>
</head>
<body>
<main class="stage">
  <section class="card card--front" aria-label="Card front">
    <div class="brand-dot"></div>
    <div class="brand">Meridian Sound Wellness<br>LLC</div>
    <div class="contact">
      <p class="contact__name">Tobias Wrenfield <span class="contact__creds">HIS COHC</span></p>
      <p>Manager</p>
      <p class="contact__block">48730 W Linden Row, Suite 9<br>Spokane, WA 99481</p>
      <p class="contact__block">509-617-2085<br>www.meridiansoundnorth.example</p>
      <p class="contact__license">License #81729046</p>
    </div>
  </section>
  <section class="card card--back" aria-label="Card back">
    <div class="brand">Meridian Sound Wellness<br>LLC</div>
  </section>
</main>
</body>
</html>
```